Company Eco-System 1 Page Graphic

We need a 1 page visual of what our company does and all of the different parts of the company and what they do.
We would like it to be as simple as possible, modern, clean.
Our logo and colour palette are attached.
We are an events management company and we want to show our shareholders a graphic that demonstrates how the different parts of our company work together to deliver events and our strategic goals

Target Market(s)

Our local Council which we are owned by

Industry/Entity Type

Events Management

Font styles to use
Other font styles liked:
• Calibri light

```html
<!DOCTYPE html>
<html lang="en">
<head>
<meta charset="utf-8">
<title>Harbourline Events – Company Eco-System</title>
<link rel="stylesheet" href="https://fonts.googleapis.com/css2?family=Source+Sans+3:wght@300;400;600&display=swap">
<style>
  :root {
    --page: #ffffff;
    --paper: #eeebe4;
    --ink: #111111;
    --core-blue: #2e57a2;
    --attract-purple: #5f3f91;
    --commercial-navy: #232544;
    --marketing-brown: #564936;
    --planning-pink: #eda0c6;
    --delivery-orange: #e9532e;
    --systems-yellow: #f5bd1f;
    --people-green: #29a744;
    --assets-red: #c1443b;
    --label-white: #ffffff;
  }
  html, body {
    margin: 0;
    padding: 0;
    width: 1200px;
    height: 1200px;
    overflow: hidden;
    background: var(--page);
  }
  .ecosystem {
    display: block;
    width: 1200px;
    height: 1200px;
    font-family: "Source Sans 3", "Calibri", sans-serif;
  }
  .paper { fill: var(--paper); }
  .divider { stroke: var(--core-blue); stroke-width: 4; stroke-dasharray: 32 20; }
  .core-ring { fill: var(--paper); stroke: var(--core-blue); stroke-width: 11; }
  .core-rule { stroke: var(--core-blue); stroke-width: 11; }
  .pillar { fill: var(--core-blue); font-size: 25px; font-weight: 300; text-anchor: middle; letter-spacing: 0.5px; }
  .company-name { fill: var(--ink); font-size: 50px; font-weight: 400; letter-spacing: 1px; text-anchor: middle; }
  .cycle-word { fill: var(--ink); font-size: 40px; font-weight: 300; letter-spacing: 2px; text-anchor: middle; dominant-baseline: central; }
  .cycle-arrow { fill: none; stroke: var(--ink); stroke-width: 3; }
  .goal { fill: var(--ink); font-size: 31px; font-weight: 300; letter-spacing: 0.5px; text-anchor: middle; }
  .link { stroke-width: 4; fill: none; }
  .label { fill: var(--label-white); text-anchor: middle; dominant-baseline: central; font-weight: 300; }
  .leaf .label { font-size: 16px; }
  .hub .label { font-size: 22px; }
  .mark-query { font-size: 44px; }

  .attract .link { stroke: var(--attract-purple); } .attract circle { fill: var(--attract-purple); }
  .commercial .link { stroke: var(--commercial-navy); } .commercial circle { fill: var(--commercial-navy); }
  .marketing .link { stroke: var(--marketing-brown); } .marketing circle { fill: var(--marketing-brown); }
  .planning .link { stroke: var(--planning-pink); } .planning circle { fill: var(--planning-pink); }
  .delivery .link { stroke: var(--delivery-orange); } .delivery circle { fill: var(--delivery-orange); }
  .systems .link { stroke: var(--systems-yellow); } .systems circle { fill: var(--systems-yellow); }
  .people .link { stroke: var(--people-green); } .people circle { fill: var(--people-green); }
  .assets .link { stroke: var(--assets-red); } .assets circle { fill: var(--assets-red); }
</style>
</head>
<body>
<svg class="ecosystem" viewBox="0 0 1932 1932" role="img" aria-label="Harbourline Events company eco-system">
  <defs>
    <marker id="arrowhead" viewBox="0 0 10 10" refX="8" refY="5" markerWidth="6" markerHeight="6" orient="auto">
      <path d="M0,0 L10,5 L0,10 z" fill="#111111"/>
    </marker>
    <path id="goal-track-outer" d="M96,966 A870,870 0 1 1 1836,966 A870,870 0 1 1 96,966"/>
    <path id="goal-track-inner" d="M76,966 A890,890 0 1 0 1856,966 A890,890 0 1 0 76,966"/>
  </defs>

  <rect width="1932" height="1932" fill="#ffffff"/>
  <circle class="paper" cx="966" cy="966" r="925"/>

  <line class="divider" x1="42" y1="966" x2="672" y2="966"/>
  <line class="divider" x1="1266" y1="966" x2="1892" y2="966"/>

  <!-- Strategic goals -->
  <text class="goal"><textPath href="#goal-track-outer" startOffset="531">CELEBRATE AND SOURCE LOCAL</textPath></text>
  <text class="goal"><textPath href="#goal-track-outer" startOffset="2208">STRATEGIC PARTNERS HIPS</textPath></text>
  <text class="goal"><textPath href="#goal-track-inner" startOffset="482">HEALTH SAFETY AND WELLBEING</textPath></text>
  <text class="goal"><textPath href="#goal-track-inner" startOffset="1398">ENVIRONMENTAL AND SOCIAL SUSTAINABILITY</textPath></text>
  <text class="goal"><textPath href="#goal-track-inner" startOffset="2366">STAKEHOLDER ENGAGEMENT</textPath></text>

  <!-- Cluster links -->
  <g class="attract"><line class="link" x1="880" y1="370" x2="913" y2="680"/></g>
  <g class="commercial"><line class="link" x1="560" y1="562" x2="753" y2="768"/></g>
  <g class="marketing"><line class="link" x1="420" y1="820" x2="678" y2="930"/></g>
  <g class="planning"><line class="link" x1="1226" y1="530" x2="1110" y2="713"/></g>
  <g class="delivery"><line class="link" x1="1469" y1="817" x2="1250" y2="900"/></g>
  <g class="systems"><line class="link" x1="1293" y1="1282" x2="1160" y2="1185"/></g>
  <g class="people"><line class="link" x1="866" y1="1452" x2="891" y2="1248"/></g>
  <g class="assets"><line class="link" x1="495" y1="1344" x2="710" y2="1104"/></g>

  <!-- Event attraction & sales -->
  <g class="cluster attract">
    <line class="link" x1="880" y1="370" x2="744" y2="215"/>
    <line class="link" x1="880" y1="370" x2="884" y2="180"/>
    <line class="link" x1="880" y1="370" x2="1022" y2="228"/>
    <line class="link" x1="880" y1="370" x2="1118" y2="332"/>
    <line class="link" x1="880" y1="370" x2="645" y2="317"/>
    <line class="link" x1="880" y1="370" x2="754" y2="552"/>
    <line class="link" x1="880" y1="370" x2="1020" y2="513"/>
    <g class="leaf"><circle cx="744" cy="215" r="60"/><text class="label" x="744" y="215">ENTERTAINMART</text></g>
    <g class="leaf"><circle cx="884" cy="180" r="53"/><text class="label" x="884" y="180">COMMUNITY</text></g>
    <g class="leaf"><circle cx="1022" cy="228" r="46"/><text class="label" x="1022" y="228"><tspan x="1022" dy="-11">LIFE</tspan><tspan x="1022" dy="22">STILE</tspan></text></g>
    <g class="leaf"><circle cx="1118" cy="332" r="46"/><text class="label" x="1118" y="332">EDUCATION</text></g>
    <g class="leaf"><circle cx="645" cy="317" r="46"/><text class="label" x="645" y="317"><tspan x="645" dy="-9">TECHNICAL</tspan><tspan x="645" dy="19">SERVICES</tspan></text></g>
    <g class="leaf"><circle cx="754" cy="552" r="46"/><text class="label" x="754" y="552">SPORT</text></g>
    <g class="leaf"><circle cx="1020" cy="513" r="46"/><text class="label" x="1020" y="513">BUSINESS</text></g>
    <g class="hub"><circle cx="880" cy="370" r="73"/><text class="label" x="880" y="370"><tspan x="882" dy="-28">EVENT</tspan><tspan x="882" dy="28">ATTRACTION</tspan><tspan x="880" dy="30">SALES</tspan></text></g>
  </g>

  <!-- Commercial -->
  <g class="cluster commercial">
    <line class="link" x1="560" y1="562" x2="418" y2="441"/>
    <line class="link" x1="560" y1="562" x2="558" y2="400"/>
    <line class="link" x1="560" y1="562" x2="706" y2="459"/>
    <line class="link" x1="560" y1="562" x2="389" y2="605"/>
    <line class="link" x1="560" y1="562" x2="576" y2="714"/>
    <g class="leaf"><circle cx="418" cy="441" r="57"/><text class="label" x="418" y="441"><tspan x="418" dy="-8">COMMERCIAL</tspan><tspan x="418" dy="17">PARINERSMMS</tspan></text></g>
    <g class="leaf"><circle cx="558" cy="400" r="46"/><text class="label" x="558" y="403">SPONSORS</text></g>
    <g class="leaf"><circle cx="706" cy="459" r="46"/><text class="label" x="706" y="459"><tspan x="706" dy="-11">REVENUE</tspan><tspan x="706" dy="22">GROW</tspan></text></g>
    <g class="leaf"><circle cx="389" cy="605" r="46"/><text class="label" x="389" y="605">MEMBERSIR</text></g>
    <g class="leaf"><circle cx="576" cy="714" r="46"/><text class="label" x="576" y="714">TICKETING</text></g>
    <g class="hub"><circle cx="560" cy="562" r="72"/><text class="label" x="560" y="560">COMMERCIAL</text></g>
  </g>

  <!-- Marketing & communications -->
  <g class="cluster marketing">
    <line class="link" x1="420" y1="820" x2="322" y2="705"/>
    <line class="link" x1="420" y1="820" x2="466" y2="686"/>
    <line class="link" x1="420" y1="820" x2="261" y2="818"/>
    <line class="link" x1="420" y1="820" x2="326" y2="914"/>
    <g class="leaf"><circle cx="322" cy="705" r="45"/><text class="label" x="322" y="705">REPUTATION</text></g>
    <g class="leaf"><circle cx="466" cy="686" r="38"/><text class="label" x="466" y="688">BRAND</text></g>
    <g class="leaf"><circle cx="261" cy="818" r="38"/><text class="label mark-query" x="261" y="815">?</text></g>
    <g class="leaf"><circle cx="326" cy="914" r="45"/><text class="label" x="326" y="914"><tspan x="326" dy="-9">PUBLIC</tspan><tspan x="326" dy="18">RELATIONS</tspan></text></g>
    <g class="hub"><circle cx="420" cy="820" r="83"/><text class="label" x="420" y="812" style="font-size:17px"><tspan x="419" dy="-21">MARKETING</tspan><tspan x="419" dy="21">AND</tspan><tspan x="420" dy="21">COMMUNICATIONS</tspan></text></g>
  </g>

  <!-- Event planning -->
  <g class="cluster planning">
    <line class="link" x1="1226" y1="530" x2="1265" y2="325"/>
    <line class="link" x1="1226" y1="530" x2="1442" y2="383"/>
    <line class="link" x1="1226" y1="530" x2="1112" y2="438"/>
    <line class="link" x1="1226" y1="530" x2="1452" y2="507"/>
    <line class="link" x1="1226" y1="530" x2="1048" y2="616"/>
    <line class="link" x1="1226" y1="530" x2="1420" y2="622"/>
    <line class="link" x1="1226" y1="530" x2="1239" y2="706"/>
    <g class="leaf"><circle cx="1265" cy="325" r="57"/><text class="label" x="1266" y="325">PROCUREMENT</text></g>
    <g class="leaf"><circle cx="1442" cy="383" r="45"/><text class="label" x="1442" y="383"><tspan x="1444" dy="-10">EVENT</tspan><tspan x="1441" dy="20">LOGISTICS</tspan></text></g>
    <g class="leaf"><circle cx="1112" cy="438" r="55"/><text class="label" x="1112" y="438"><tspan x="1111" dy="-10">CLIENT</tspan><tspan x="1113" dy="20">ENGAGEMENT</tspan></text></g>
    <g class="leaf"><circle cx="1452" cy="507" r="50"/><text class="label" x="1450" y="507">RESOURCING</text></g>
    <g class="leaf"><circle cx="1048" cy="616" r="45"/><text class="label" x="1048" y="618"><tspan x="1048" dy="-19">HEALTH</tspan><tspan x="1048" dy="19">AND</tspan><tspan x="1048" dy="19">SAFETY</tspan></text></g>
    <g class="leaf"><circle cx="1420" cy="622" r="45"/><text class="label" x="1420" y="622"><tspan x="1420" dy="-18">RETAIL</tspan><tspan x="1420" dy="18">MENU</tspan><tspan x="1421" dy="18">DESIGN</tspan></text></g>
    <g class="leaf"><circle cx="1239" cy="706" r="45"/><text class="label" x="1239" y="711"><tspan x="1239" dy="-17">CORPORATE</tspan><tspan x="1239" dy="17">MENU</tspan><tspan x="1238" dy="17">DESIGN</tspan></text></g>
    <g class="hub"><circle cx="1226" cy="530" r="73"/><text class="label" x="1226" y="521"><tspan x="1226" dy="-20">EVENT</tspan><tspan x="1226" dy="20">PLANNING</tspan><tspan x="1227" dy="20">MANAGENSTS</tspan></text></g>
  </g>

  <!-- Event delivery -->
  <g class="cluster delivery">
    <line class="link" x1="1469" y1="817" x2="1548" y2="575"/>
    <line class="link" x1="1469" y1="817" x2="1697" y2="605"/>
    <line class="link" x1="1469" y1="817" x2="1353" y2="717"/>
    <line class="link" x1="1469" y1="817" x2="1721" y2="741"/>
    <line class="link" x1="1469" y1="817" x2="1266" y2="815"/>
    <line class="link" x1="1469" y1="817" x2="1746" y2="862"/>
    <line class="link" x1="1469" y1="817" x2="1390" y2="918"/>
    <line class="link" x1="1469" y1="817" x2="1607" y2="903"/>
    <g class="leaf"><circle cx="1548" cy="575" r="52"/><text class="label" x="1548" y="575"><tspan x="1548" dy="-16">CORPORATE</tspan><tspan x="1548" dy="16">FOODAND</tspan><tspan x="1547" dy="16">BEVERAGE</tspan></text></g>
    <g class="leaf"><circle cx="1697" cy="605" r="52"/><text class="label" x="1697" y="603"><tspan x="1697" dy="-16">RETAIL</tspan><tspan x="1697" dy="16">FOOD AND</tspan><tspan x="1697" dy="16">BEVERAGE</tspan></text></g>
    <g class="leaf"><circle cx="1353" cy="717" r="55"/><text class="label" x="1353" y="713"><tspan x="1353" dy="-8">EMERGENCY</tspan><tspan x="1353" dy="16">MANAGEMENT</tspan></text></g>
    <g class="leaf"><circle cx="1721" cy="741" r="53"/><text class="label" x="1721" y="740"><tspan x="1722" dy="-10">HITCHEN</tspan><tspan x="1721" dy="20">OPERATIONS</tspan></text></g>
    <g class="leaf"><circle cx="1266" cy="815" r="45"/><text class="label" x="1266" y="815">HOSTING</text></g>
    <g class="leaf"><circle cx="1746" cy="862" r="58"/><text class="label" x="1746" y="857"><tspan x="1746" dy="-10">VENUE</tspan><tspan x="1746" dy="20">MANAGEMENT</tspan></text></g>
    <g class="leaf"><circle cx="1390" cy="918" r="45"/><text class="label" x="1390" y="918">CLEANING</text></g>
    <g class="leaf"><circle cx="1607" cy="903" r="58"/><text class="label" x="1607" y="899"><tspan x="1607" dy="-10">TRAFFIC</tspan><tspan x="1607" dy="20">MANAGEMENT</tspan></text></g>
    <g class="hub"><circle cx="1469" cy="817" r="73"/><text class="label" x="1469" y="812"><tspan x="1469" dy="-24">EVENT</tspan><tspan x="1470" dy="24">DELIVERY</tspan><tspan x="1467" dy="24">OPERATIONS</tspan></text></g>
  </g>

  <!-- Systems, policies & procedures -->
  <g class="cluster systems">
    <line class="link" x1="1293" y1="1282" x2="1270" y2="1133"/>
    <line class="link" x1="1293" y1="1282" x2="1424" y2="1124"/>
    <line class="link" x1="1293" y1="1282" x2="1541" y2="1229"/>
    <line class="link" x1="1293" y1="1282" x2="1142" y2="1350"/>
    <line class="link" x1="1293" y1="1282" x2="1560" y2="1379"/>
    <line class="link" x1="1293" y1="1282" x2="1250" y2="1488"/>
    <line class="link" x1="1293" y1="1282" x2="1438" y2="1495"/>
    <g class="leaf"><circle cx="1270" cy="1133" r="45"/><text class="label" x="1270" y="1135"><tspan x="1268" dy="-10">FINANCE</tspan><tspan x="1270" dy="20">PLANNING</tspan></text></g>
    <g class="leaf"><circle cx="1424" cy="1124" r="50"/><text class="label" x="1424" y="1123"><tspan x="1425" dy="-8">STATUTORY</tspan><tspan x="1423" dy="17">COMPLIANCE</tspan></text></g>
    <g class="leaf"><circle cx="1541" cy="1229" r="45"/><text class="label" x="1541" y="1229">POLICIES</text></g>
    <g class="leaf"><circle cx="1142" cy="1350" r="50"/><text class="label" x="1142" y="1352">PROCEDURES</text></g>
    <g class="leaf"><circle cx="1560" cy="1379" r="45"/><text class="label" x="1562" y="1379">PAYROLL</text></g>
    <g class="leaf"><circle cx="1250" cy="1488" r="45"/><text class="label" x="1248" y="1488">ICT</text></g>
    <g class="leaf"><circle cx="1438" cy="1495" r="60"/><text class="label" x="1440" y="1495"><tspan x="1439" dy="-19">ACCOUNTS</tspan><tspan x="1441" dy="19">PAYABLE</tspan><tspan x="1441" dy="19">RECERVABLE</tspan></text></g>
    <g class="hub"><circle cx="1293" cy="1282" r="73"/><text class="label" x="1293" y="1286" style="font-size:18px"><tspan x="1292" dy="-20">SYSTEMS</tspan><tspan x="1293" dy="19">POLICIES</tspan><tspan x="1296" dy="23">PROCEDURES</tspan></text></g>
  </g>

  <!-- People & culture -->
  <g class="cluster people">
    <line class="link" x1="866" y1="1452" x2="771" y2="1270"/>
    <line class="link" x1="866" y1="1452" x2="1001" y2="1331"/>
    <line class="link" x1="866" y1="1452" x2="672" y2="1364"/>
    <line class="link" x1="866" y1="1452" x2="1074" y2="1507"/>
    <line class="link" x1="866" y1="1452" x2="736" y2="1613"/>
    <line class="link" x1="866" y1="1452" x2="966" y2="1634"/>
    <g class="leaf"><circle cx="771" cy="1270" r="57"/><text class="label" x="771" y="1270"><tspan x="770" dy="-10">CAPABILITY</tspan><tspan x="771" dy="20">DEVELOPMENT</tspan></text></g>
    <g class="leaf"><circle cx="1001" cy="1331" r="45"/><text class="label" x="1001" y="1331">CULTURE</text></g>
    <g class="leaf"><circle cx="672" cy="1364" r="45"/><text class="label" x="672" y="1364">ROSTERING</text></g>
    <g class="leaf"><circle cx="1074" cy="1507" r="62"/><text class="label" x="1074" y="1511"><tspan x="1075" dy="-22">RECRUITMENT</tspan><tspan x="1074" dy="20">AND</tspan><tspan x="1074" dy="25">RETENTION</tspan></text></g>
    <g class="leaf"><circle cx="736" cy="1613" r="62"/><text class="label" x="736" y="1617"><tspan x="737" dy="-18">COMUNICATION</tspan><tspan x="733" dy="18">AND</tspan><tspan x="736" dy="18">ENGAGEMENT</tspan></text></g>
    <g class="leaf"><circle cx="966" cy="1634" r="45"/><text class="label" x="966" y="1634">WELLBEING</text></g>
    <g class="hub"><circle cx="866" cy="1452" r="73"/><text class="label" x="864" y="1450"><tspan x="864" dy="-26">PEOPLE</tspan><tspan x="863" dy="25">AND</tspan><tspan x="862" dy="27">CULTURE</tspan></text></g>
  </g>

  <!-- Assets & facilities -->
  <g class="cluster assets">
    <line class="link" x1="495" y1="1344" x2="512" y2="1098"/>
    <line class="link" x1="495" y1="1344" x2="331" y2="1166"/>
    <line class="link" x1="495" y1="1344" x2="275" y2="1346"/>
    <line class="link" x1="495" y1="1344" x2="645" y2="1483"/>
    <line class="link" x1="495" y1="1344" x2="401" y2="1530"/>
    <g class="leaf"><circle cx="512" cy="1098" r="45"/><text class="label" x="512" y="1104"><tspan x="511" dy="-10">REACTIVE</tspan><tspan x="514" dy="21">MAINTENANCE</tspan></text></g>
    <g class="leaf"><circle cx="331" cy="1166" r="45"/><text class="label" x="334" y="1168"><tspan x="334" dy="-9">PRESENTATION</tspan><tspan x="334" dy="19">MAINTENANCE</tspan></text></g>
    <g class="leaf"><circle cx="275" cy="1346" r="62"/><text class="label" x="275" y="1347"><tspan x="274" dy="-13">CAPITAL</tspan><tspan x="275" dy="27">PROGRAMME</tspan></text></g>
    <g class="leaf"><circle cx="645" cy="1483" r="45"/><text class="label" x="645" y="1483"><tspan x="644" dy="-16">EVENT</tspan><tspan x="643" dy="16">DAY</tspan><tspan x="646" dy="16">RESPONSE</tspan></text></g>
    <g class="leaf"><circle cx="401" cy="1530" r="45"/><text class="label" x="401" y="1526"><tspan x="401" dy="-10">VENUE</tspan><tspan x="398" dy="19">PRESENTATION</tspan></text></g>
    <g class="hub"><circle cx="495" cy="1344" r="73"/><text class="label" x="495" y="1344"><tspan x="497" dy="-22">ASSTS AND</tspan><tspan x="495" dy="24">FACILITIES</tspan><tspan x="495" dy="20" style="font-size:17px">MANAGEMENT</tspan></text></g>
  </g>

  <!-- Operating cycle -->
  <g class="cycle">
    <text class="cycle-word" transform="translate(765 822) rotate(-55)">ATTRACT</text>
    <text class="cycle-word" transform="translate(960 718) rotate(2)">PLAN</text>
    <text class="cycle-word" transform="translate(1157 810) rotate(53)">DELIVER</text>
    <text class="cycle-word" transform="translate(1183 1092) rotate(-58)">PROTECT</text>
    <text class="cycle-word" transform="translate(962 1228) rotate(3)">ENABLE</text>
    <text class="cycle-word" transform="translate(746 1088) rotate(58)">PREPARE</text>

    <path class="cycle-arrow" d="M822,752 Q855,730 898,724" marker-end="url(#arrowhead)"/>
    <path class="cycle-arrow" d="M1026,720 Q1072,732 1102,764" marker-end="url(#arrowhead)"/>
    <path class="cycle-arrow" d="M1206,902 Q1220,940 1220,984" marker-end="url(#arrowhead)"/>
    <path class="cycle-arrow" d="M1126,1166 Q1100,1192 1060,1220" marker-end="url(#arrowhead)"/>
    <path class="cycle-arrow" d="M868,1208 Q828,1196 796,1166" marker-end="url(#arrowhead)"/>
    <path class="cycle-arrow" d="M712,996 Q706,950 718,910" marker-end="url(#arrowhead)"/>
  </g>

  <!-- Core -->
  <g class="core">
    <circle class="core-ring" cx="966" cy="966" r="225"/>
    <line class="core-rule" x1="741" y1="966" x2="1191" y2="966"/>
    <line class="core-rule" x1="893" y1="966" x2="893" y2="1176"/>
    <line class="core-rule" x1="1047" y1="966" x2="1047" y2="1176"/>
    <text class="company-name" x="966" y="870">HARBOURLINE</text>
    <text class="company-name" x="966" y="926">EVENTS</text>
    <text class="pillar" x="820" y="1012">VENUES</text>
    <text class="pillar" x="968" y="1012">PEOPLE</text>
    <text class="pillar" x="1114" y="1012">SYSTEMS</text>
  </g>
</svg>
</body>
</html>
```